Post COVID-19 Infographic - As the economy begins to rebound, you need to be ready to upgrade your f

Due to the COVID-19 Pandemic, many of these businesses are shut down or operating with essential staff while the remaining personnel are working from home.

As we are reaching the peak of the pandemic, many businesses are starting to think about what they need to do in their facilities to retrofit them and make them safe for their employees and customers in a post COVID-19 world.
This assignment is about developing an infographic that will provide our current and potential customers with information about the old world, and the new world. This needs to be interesting, informational, and viral (i.e.- content is so compelling folks will share with friends, colleagues and other businesses.

Please see attached for a full fledged creative brief.

Target Market(s)

Distribution Centers, manufacturers, Multi-family Housing property managers, Home Owner Associations, Small to Medium Sized Businesses

Industry/Entity Type

Distributor

Font styles to use
Sans Serif

Requirements
Must have
• Graphical, easy to understand, fun to read, trigger thinking, reader would want to share with friends, colleagues, online

Colors should be similar to color palette used on our website www.marlowsupplyhub.com
Nice to have
• Iconography
Should not have
• Should not appear like we are trying to sell. Should look informational but should be clear that we can supply those products

```html
<!DOCTYPE html>
<html lang="en">
<head>
<meta charset="utf-8">
<title>Post COVID-19 – How to protect customers &amp; office employees</title>
<link href="https://fonts.googleapis.com/css2?family=Barlow+Condensed:wght@700&family=Fira+Sans:wght@400;500&display=swap" rel="stylesheet">
<style>
  :root {
    --navy: #0b5a78;
    --navy-dark: #0a4f6b;
    --teal: #0aa08f;
    --card: #f0f0f0;
    --white: #ffffff;
  }
  * { margin: 0; padding: 0; box-sizing: border-box; }
  html, body { width: 844px; height: 1200px; overflow: hidden; background: var(--white); }
  body { font-family: "Fira Sans", sans-serif; color: var(--navy); }
  .poster { position: relative; width: 844px; height: 1200px; }

  .poster-title {
    position: absolute; top: 30px; left: 0; width: 800px; text-align: center;
    font-family: "Barlow Condensed", sans-serif; font-weight: 700;
    font-size: 56px; letter-spacing: 1px; color: var(--navy-dark); line-height: 1;
  }
  .subtitle-band {
    position: absolute; left: 292px; top: 117px; width: 552px; height: 89px;
    background: var(--navy); border-radius: 14px 0 0 14px;
    color: var(--white); font-weight: 500; font-size: 29px; line-height: 42px;
    text-align: right; padding: 3px 34px 0 0;
  }
  .section-band {
    position: absolute; left: 0; height: 54px; background: var(--navy);
    border-radius: 0 27px 27px 0; color: var(--white);
    font-size: 28px; font-weight: 500; line-height: 54px; padding-left: 21px;
  }
  .section-band--good { top: 238px; width: 406px; }
  .section-band--bad { top: 711px; width: 385px; }

  .tip { position: absolute; width: 407px; height: 132px; }
  .tip--left { left: 21px; }
  .tip--right { left: 444px; }
  .tip__icon { position: absolute; left: 0; top: 0; width: 114px; height: 132px; }
  .tip__bracket { position: absolute; left: 107px; top: 0; width: 16px; height: 132px; }
  .tip__card {
    position: absolute; left: 114px; top: 0; right: 0; height: 132px;
    background: var(--card); padding: 18px 8px 0 26px;
  }
  .tip--right .tip__card { right: -4px; }
  .tip__heading { font-size: 23px; font-weight: 500; color: var(--navy-dark); line-height: 1.2; }
  .tip__text { margin-top: 12px; font-size: 17px; line-height: 24px; color: var(--navy); }

  .brand {
    position: absolute; left: 630px; top: 1138px; display: flex; align-items: center; gap: 8px;
    font-size: 22px; font-weight: 500; color: var(--navy-dark);
  }
  .brand__mark { width: 14px; height: 14px; border-radius: 50%; background: var(--navy-dark); }
  .brand__url { position: absolute; left: 652px; top: 1168px; font-size: 14px; font-weight: 500; color: var(--navy-dark); }
</style>
</head>
<body>
<svg width="0" height="0" style="position:absolute">
  <defs>
    <linearGradient id="hex-fill" x1="0" y1="0" x2="1" y2="1">
      <stop offset="0" stop-color="#0aa895"/>
      <stop offset="1" stop-color="#0b5a78"/>
    </linearGradient>
  </defs>
</svg>
<main class="poster">
  <h1 class="poster-title">POST COVID-19</h1>
  <div class="subtitle-band">How to protect customers &amp;<br>office employees from infection</div>

  <div class="section-band section-band--good">Follow these good practices</div>

  <div class="tip tip--left" style="top:348px">
    <svg class="tip__icon" viewBox="0 0 114 132" role="img" aria-label="Hands washing under a tap"><polygon points="57,0 114,33 114,99 57,132 0,99 0,33" fill="url(#hex-fill)"/></svg>
    <svg class="tip__bracket" viewBox="0 0 16 132"><polyline points="14,2 5,2 5,130 14,130" fill="none" stroke="var(--navy)" stroke-width="6"/></svg>
    <div class="tip__card"><h2 class="tip__heading">Wash hands oftenly</h2><p class="tip__text">Wash your hands oftenly<br>with soap.</p></div>
  </div>
  <div class="tip tip--right" style="top:348px">
    <svg class="tip__icon" viewBox="0 0 114 132" role="img" aria-label="Hand holding a disinfectant spray bottle"><polygon points="57,0 114,33 114,99 57,132 0,99 0,33" fill="url(#hex-fill)"/></svg>
    <svg class="tip__bracket" viewBox="0 0 16 132"><polyline points="14,2 5,2 5,130 14,130" fill="none" stroke="var(--navy)" stroke-width="6"/></svg>
    <div class="tip__card"><h2 class="tip__heading">Clean and disinfect</h2><p class="tip__text">Facilities cleaned many<br>times a day</p></div>
  </div>

  <div class="tip tip--left" style="top:519px">
    <svg class="tip__icon" viewBox="0 0 114 132" role="img" aria-label="Person covering mouth while sneezing"><polygon points="57,0 114,33 114,99 57,132 0,99 0,33" fill="url(#hex-fill)"/></svg>
    <svg class="tip__bracket" viewBox="0 0 16 132"><polyline points="14,2 5,2 5,130 14,130" fill="none" stroke="var(--navy)" stroke-width="6"/></svg>
    <div class="tip__card" style="padding-left:16px"><h2 class="tip__heading">Cover while sneezing</h2><p class="tip__text" style="padding-left:10px">Cover mouth &amp; nose while<br>caughing or sneezing.</p></div>
  </div>
  <div class="tip tip--right" style="top:519px">
    <svg class="tip__icon" viewBox="0 0 114 132" role="img" aria-label="Person wearing a face mask"><polygon points="57,0 114,33 114,99 57,132 0,99 0,33" fill="url(#hex-fill)"/></svg>
    <svg class="tip__bracket" viewBox="0 0 16 132"><polyline points="14,2 5,2 5,130 14,130" fill="none" stroke="var(--navy)" stroke-width="6"/></svg>
    <div class="tip__card"><h2 class="tip__heading" style="padding-left:30px">Hide your face</h2><p class="tip__text">Hide your face with face<br>mask for self protection.</p></div>
  </div>

  <div class="section-band section-band--bad">Avoid these bad practices</div>

  <div class="tip tip--left" style="top:800px">
    <svg class="tip__icon" viewBox="0 0 114 132" role="img" aria-label="Two hands shaking"><polygon points="57,0 114,33 114,99 57,132 0,99 0,33" fill="url(#hex-fill)"/></svg>
    <svg class="tip__bracket" viewBox="0 0 16 132"><polyline points="14,2 5,2 5,130 14,130" fill="none" stroke="var(--navy)" stroke-width="6"/></svg>
    <div class="tip__card"><h2 class="tip__heading" style="padding-left:10px">Avoid handshakes</h2><p class="tip__text">Avoid direct contact with<br>other person.</p></div>
  </div>
  <div class="tip tip--right" style="top:800px">
    <svg class="tip__icon" viewBox="0 0 114 132" role="img" aria-label="Crowd of people standing together"><polygon points="57,0 114,33 114,99 57,132 0,99 0,33" fill="url(#hex-fill)"/></svg>
    <svg class="tip__bracket" viewBox="0 0 16 132"><polyline points="14,2 5,2 5,130 14,130" fill="none" stroke="var(--navy)" stroke-width="6"/></svg>
    <div class="tip__card"><h2 class="tip__heading" style="padding-left:20px">Public gathering</h2><p class="tip__text" style="padding-left:10px">Avoid social gathering<br>for self protection.</p></div>
  </div>

  <div class="tip tip--left" style="top:970px">
    <svg class="tip__icon" viewBox="0 0 114 132" role="img" aria-label="Farm animals silhouettes"><polygon points="57,0 114,33 114,99 57,132 0,99 0,33" fill="url(#hex-fill)"/></svg>
    <svg class="tip__bracket" viewBox="0 0 16 132"><polyline points="14,2 5,2 5,130 14,130" fill="none" stroke="var(--navy)" stroke-width="6"/></svg>
    <div class="tip__card"><h2 class="tip__heading" style="padding-left:10px">Avoid animals</h2><p class="tip__text">Avoid direct contact with<br>farm &amp; wild animals.</p></div>
  </div>
  <div class="tip tip--right" style="top:970px">
    <svg class="tip__icon" viewBox="0 0 114 132" role="img" aria-label="Sick person sneezing"><polygon points="57,0 114,33 114,99 57,132 0,99 0,33" fill="url(#hex-fill)"/></svg>
    <svg class="tip__bracket" viewBox="0 0 16 132"><polyline points="14,2 5,2 5,130 14,130" fill="none" stroke="var(--navy)" stroke-width="6"/></svg>
    <div class="tip__card" style="padding-left:24px"><h2 class="tip__heading">Avoid affected person</h2><p class="tip__text" style="padding-left:15px">Keep safe distance from<br>a flu affected person.</p></div>
  </div>

  <div class="brand"><span class="brand__mark"></span><span>MARLOW</span></div>
  <div class="brand__url">www.marlowsupplyhub.com</div>
</main>
</body>
</html>
```